Recruitment of Brindle Crew Staffing for the UK market

I want a website for the UK market to attract businesses and companies to come to us for Philipine labour. We want an information site that gives all information on what we do and how we can recruit Philippine labour.
This is a recruitment site for companies to contact us with their requirements for skilled workers coming from the Philipines over to the UK to work.

Target Market(s)

Uk Companies and businesses who want Philipine skilled workers

Industry/Entity Type

REcruitment

Coding

Coded - Design and coding required

Number of Pages Required

5+ page

Font styles to use
Sans Serif

Colors
0054AA
0677BA
7BADD7
CADEEF
E8F1F8
0094D4
00A9DD
6FCCEA
C7EBF8
E9F6FB
EE7325
F08F49
F5BC92
FAE3D3
FDF4ED
EB3D1F
EC4F4E
F09395
F8D3D4
FCEDEE

Requirements
Must have
• Look professional and corperate with drop down menus for Home ,about, services,articles. training , contact us
Nice to have
• Look at Tolvane recruitment- https://tolvanerecruitment.example.co.uk/. This is my current site - https://www.brindlecrewstaffing.example.com/
Should not have
• Cartoons or silly pictures , needs to be corperate looking

```html
<!DOCTYPE html>
<html lang="en">
<head>
<meta charset="UTF-8">
<title>Brindle Crew Staffing – Recruiting and Placing</title>
<link href="https://fonts.googleapis.com/css2?family=Rubik:wght@400;500;600&family=DM+Sans:wght@400;500;700&display=swap" rel="stylesheet">
<style>
:root{
  --red:#912f2c;
  --red-dark:#7a2522;
  --navy:#16163a;
  --text:#3b3b55;
  --muted:#6b6b80;
  --lavender:#f6f5fc;
  --line:#e2e2ea;
  --footer:#1b1a2c;
  --white:#ffffff;
}
*{box-sizing:border-box;margin:0;padding:0}
html,body{width:1200px;height:5398px;overflow:hidden}
body{position:relative;font-family:"DM Sans",sans-serif;color:var(--text);background:var(--white);font-size:14px;line-height:1.6}
.abs{position:absolute}
h1,h2,h3,h4{font-family:"Rubik",sans-serif;color:var(--navy);font-weight:500}
.eyebrow{font-family:"DM Sans",sans-serif;font-size:13px;font-weight:700;color:var(--red);text-transform:uppercase;letter-spacing:.02em}
.section-title{font-size:48px;line-height:1.2;font-weight:500}
.btn{display:inline-flex;align-items:center;gap:10px;font-size:14px;font-weight:700;text-transform:uppercase;border-radius:30px;text-decoration:none}
.btn-red{background:var(--red);color:var(--white);padding:0 26px;height:46px}
.btn-outline{border:1px solid var(--red);color:var(--red);border-radius:4px;padding:0 20px;height:50px;text-transform:none;font-weight:500;font-size:15px}
.arrow{font-size:14px;letter-spacing:-2px}

/* header */
.site-header{left:0;top:0;width:1200px;height:100px;background:var(--white)}
.logo{font-family:"Rubik",sans-serif;font-weight:600;font-size:22px;color:var(--red);display:flex;align-items:center;gap:10px}
.logo .mark{width:16px;height:16px;background:var(--red)}
.site-header .logo{left:100px;top:34px}
.main-nav{left:366px;top:38px;display:flex;gap:28px;font-size:14px;font-weight:500;color:var(--navy);text-transform:uppercase}
.main-nav .active{color:var(--red);position:relative}
.main-nav .active::after{content:"";position:absolute;left:0;right:0;bottom:-8px;height:3px;background:var(--red)}
.upload-btn{left:918px;top:26px;height:48px;padding:0 22px}

/* hero */
.hero{left:0;top:100px;width:1200px;height:557px;background:linear-gradient(110deg,#d9e6ee 0%,#b7cfdc 45%,#a9c5d6 100%)}
.hero-title{left:737px;top:150px;font-size:56px;line-height:1.18;font-weight:600;color:var(--white);white-space:nowrap}
.hero-title span{color:var(--red)}
.hero-sub{left:737px;top:298px;font-size:16px;color:var(--navy)}
.hero-btn{left:742px;top:347px}
.hero-dots{left:562px;top:518px;display:flex;gap:8px;align-items:center}
.hero-dots i{display:block;width:8px;height:8px;border-radius:50%;background:#f0d5d4}
.hero-dots i:first-child{width:36px;border-radius:6px;background:var(--red)}

/* services */
.services .eyebrow{left:98px;top:790px}
.services h2{left:98px;top:812px;white-space:nowrap}
.services .intro{left:572px;top:838px;width:300px;font-size:14px;color:var(--text)}
.services .btn-outline{left:909px;top:856px}
.card{top:982px;width:317px;height:300px;border:1px solid var(--line);border-radius:6px;padding:34px 30px}
.card .icon{width:70px;height:70px;border:3px solid var(--red);border-radius:12px;margin-bottom:18px}
.card h3{font-size:18px;margin-bottom:12px}
.card p{font-size:14px;line-height:1.65;margin-bottom:18px;color:var(--muted)}
.card .more{font-size:14px;font-weight:700;color:var(--red);text-transform:uppercase}
.card.featured{background:var(--red);border-color:var(--red)}
.card.featured .icon{border-color:var(--white)}
.card.featured h3,.card.featured p,.card.featured .more{color:var(--white)}

/* about */
.about{left:0;top:1377px;width:1200px;height:583px;background:var(--lavender)}
.about-photo{left:98px;top:39px;width:486px;height:464px;border-radius:14px;background:linear-gradient(135deg,#c9d7d3,#8f9c98 55%,#5b5f5d)}
.visitors{left:410px;top:320px;width:130px;height:90px;background:var(--white);border-radius:6px;box-shadow:0 6px 20px rgba(0,0,0,.08);padding:16px 12px;font-size:13px;font-weight:700;color:var(--navy)}
.visitors .badge{width:26px;height:20px;background:#f3d3d2;border-radius:4px;margin-bottom:6px}
.visitors .bar{width:90px;height:3px;background:#e9a24a;margin-top:6px}
.about .eyebrow{left:668px;top:93px}
.about h2{left:668px;top:112px;white-space:nowrap}
.about p{left:668px;top:240px;width:440px;font-size:15px;line-height:1.65}
.about .btn{left:669px;top:378px}

/* working together */
.together-head{left:0;top:2020px;width:1200px;text-align:center}
.together-head h2{margin-top:6px}
.together-head p{font-size:13px;color:var(--navy);margin-top:10px}
.feature h3{font-size:24px;font-weight:500;margin-bottom:14px}
.feature p{font-size:14px;line-height:1.72;color:var(--text)}
.blob{border-radius:58% 42% 46% 54% / 44% 52% 48% 56%}
.ring{width:18px;height:18px;border:2px solid var(--red);border-radius:50%}
.cross{color:var(--red);font-size:26px;line-height:1;font-weight:700}
.dot{width:5px;height:5px;border-radius:50%;background:var(--red)}

/* news */
.news{left:0;top:3932px;width:1200px;height:528px;background:var(--lavender)}
.tag{left:98px;top:97px;height:34px;width:300px;background:var(--white);border-radius:20px;display:flex;align-items:center;gap:12px;padding:0 10px;font-size:11px;color:var(--muted)}
.tag b{background:var(--red);color:var(--white);font-size:10px;padding:2px 10px;border-radius:12px}
.news h2{left:98px;top:160px;font-size:48px;line-height:1.12;white-space:nowrap;z-index:2}
.news .lead{left:98px;top:338px;width:300px;font-size:14px;line-height:1.6}
.news-photo{left:430px;top:65px;width:342px;height:405px;background:linear-gradient(160deg,#e4e9ee,#9fa8b3 55%,#3b4150)}
.continue{left:430px;top:436px;font-size:14px;font-weight:700;color:var(--red);background:var(--lavender);padding:4px 20px 4px 0}
.news-list{left:801px;top:104px;width:300px}
.news-item{border-bottom:1px solid var(--line);padding-bottom:22px;margin-bottom:18px;display:flex;justify-content:space-between}
.news-item:last-child{border:0}
.news-item small{display:block;font-size:11px;color:var(--red);text-transform:uppercase;margin-bottom:4px}
.news-item h4{font-size:19px;line-height:1.35;font-weight:500}
.news-item .arrow{color:var(--red);margin-top:24px}

/* contact */
.contact-head{left:0;top:4490px;width:1200px;text-align:center}
.contact-head h2{font-size:46px;margin-top:2px}
.shy{left:98px;top:4590px;width:400px}
.shy h3{font-size:22px;margin-bottom:16px}
.shy p{font-size:14px;line-height:1.6;margin-bottom:22px}
.reach{display:flex;flex-direction:column;font-size:14px;color:var(--navy);margin-bottom:22px;line-height:1.45}
.reach svg{margin-bottom:4px}
.field{border:1px solid #b9b9c6;border-radius:6px;height:50px;padding:12px 10px;font-size:14px;color:var(--navy)}
.f1{left:576px;top:4590px;width:258px}
.f2{left:843px;top:4590px;width:258px}
.f3{left:576px;top:4653px;width:258px}
.f4{left:843px;top:4653px;width:258px}
.f5{left:576px;top:4716px;width:525px;height:108px}
.submit{left:576px;top:4832px;height:48px;padding:0 28px}

/* footer */
.footer{left:0;top:4922px;width:1200px;height:476px;background:var(--footer);color:#c9c9d6}
.footer .logo{left:100px;top:48px;color:var(--white)}
.footer .logo .mark{background:var(--white)}
.back-top{left:976px;top:62px;color:#e0554f;font-size:15px}
.footer-rule{left:100px;top:110px;width:1000px;height:1px;background:#34334a}
.fcol h4{color:var(--white);font-size:15px;font-weight:500;margin-bottom:18px;font-family:"DM Sans",sans-serif}
.fcol li{list-style:none;font-size:13px;line-height:34px}
.col1{left:100px;top:160px}
.col2{left:331px;top:160px}
.col3{left:813px;top:160px;width:288px}
.subscribe{display:flex;justify-content:space-between;align-items:center;border-bottom:1px solid #4a4960;padding-bottom:8px;margin-top:20px;font-size:12px;color:#5d5c75}
.subscribe i{width:26px;height:26px;border-radius:50%;background:#e0554f;display:flex;align-items:center;justify-content:center;color:var(--white);font-style:normal;font-size:13px}
.socials{display:flex;gap:16px;margin-top:34px}
.socials span{width:16px;height:16px;border-radius:50%;border:2px solid var(--white)}
.copyright{left:100px;top:422px;font-size:13px;color:#8a8a9e}
.copyright b{color:#e0554f;font-weight:400}
.stamp{left:928px;top:422px;font-size:13px;color:#8a8a9e}
</style>
</head>
<body>

<header class="site-header abs">
  <div class="logo abs"><span class="mark"></span>Brindle Crew Staffing</div>
  <nav class="main-nav abs">
    <span class="active">Home</span><span>About</span><span>Services ⌄</span><span>Articles</span><span>Training</span><span>Contact Us</span>
  </nav>
  <a class="btn btn-red upload-btn abs" href="#">Upload Resume <span>⇧</span></a>
</header>

<section class="hero abs" role="img" aria-label="Photo of two businesswomen shaking hands across a meeting table while a colleague watches">
  <h1 class="hero-title abs"><span>Recruiting</span> and<br>Placing</h1>
  <p class="hero-sub abs">Skilled Philippine Workers into UK Companies</p>
  <a class="btn btn-red hero-btn abs" href="#">Learn More <span class="arrow">→|</span></a>
  <div class="hero-dots abs"><i></i><i></i><i></i></div>
</section>

<section class="services">
  <p class="eyebrow abs">Services</p>
  <h2 class="section-title abs">Start Building your<br>Dream Career</h2>
  <p class="intro abs">Lorem ipsum dolor sit amet, consectetur adipiscing elit. Donec laoreet eget eros quis consectetur. Nullam risus ipsum,</p>
  <a class="btn btn-outline abs" href="#">View All Services <span class="arrow">→|</span></a>
  <article class="card featured abs" style="left:98px">
    <div class="icon"></div>
    <h3>Public Health Engineer</h3>
    <p>Lorem ipsum dolor sit, coectetur adipiscing elit. Donec laoreet eget eos quis</p>
    <span class="more">Learn More <span class="arrow">→|</span></span>
  </article>
  <article class="card abs" style="left:442px">
    <div class="icon"></div>
    <h3>Archaeologist</h3>
    <p>Lorem ipsum dolor sit am cotetur adipiscing elit. Donec laoreet eget eos quis</p>
    <span class="more">Learn More <span class="arrow">→|</span></span>
  </article>
  <article class="card abs" style="left:786px">
    <div class="icon"></div>
    <h3>Criminologist</h3>
    <p>Lorem ipsum dolor sit a coectetur adipiscing elit. Donec laoreet eget eos quis</p>
    <span class="more">Learn More <span class="arrow">→|</span></span>
  </article>
</section>

<section class="about abs">
  <div class="about-photo abs" role="img" aria-label="Photo of a businessman in glasses working on a laptop in a bright office"></div>
  <div class="visitors abs"><div class="badge"></div>Daily Visitors<div class="bar"></div></div>
  <p class="eyebrow abs">About Us</p>
  <h2 class="section-title abs">What the business<br>is about</h2>
  <p class="abs">We source skilled workers directly from the Philippines to work in the UK. With offices , training locations and specialist recruiters we can find the highest quality individuals to add value and resources to any UK business.</p>
  <a class="btn btn-red abs" href="#">Read More <span class="arrow">→|</span></a>
</section>

<section class="together">
  <div class="together-head abs">
    <p class="eyebrow">Working Together</p>
    <h2 class="section-title">We Recruit the Finest<br>Talent Available</h2>
    <p>with our dedicated 200 strong team. Our centres are highlighted in red dots on the map.</p>
  </div>

  <div class="feature abs" style="left:98px;top:2350px;width:485px">
    <h3>What we do</h3>
    <p>Our company has been estabilished in the Philippines for over 20 years. We have mainly been recruiting philippine workers for the off shore industry in asia but since brexit and the new rules on skilled workers entering the UK we have been working with UK companies who now have chance to recruit some of the finest hard working talent from the Philippines for their companies..</p>
  </div>
  <div class="blob abs" style="left:650px;top:2260px;width:435px;height:340px;background:linear-gradient(135deg,#e2d4c3,#b78a5a 45%,#2b3550)" role="img" aria-label="Photo of a smiling young woman with folded arms"></div>
  <span class="cross abs" style="left:1043px;top:2225px">×</span>
  <span class="ring abs" style="left:706px;top:2592px"></span>

  <div class="blob abs" style="left:95px;top:2660px;width:435px;height:330px;background:linear-gradient(135deg,#3a4f6e,#7d8ea4 50%,#1e2840)" role="img" aria-label="Photo of a smiling man in a suit holding a laptop"></div>
  <span class="ring abs" style="left:158px;top:2638px"></span>
  <span class="ring abs" style="left:540px;top:2810px"></span>
  <span class="dot abs" style="left:172px;top:3012px"></span>
  <div class="feature abs" style="left:613px;top:2745px;width:490px">
    <h3>How we help</h3>
    <p>We work with companies to find skilled workers that meet the UK requirements for Visas and work permits. We guide you through the whole process and deliver highly trained people that add value to your business. We are here to help both the companies and the Philippino people to gain a better standard of living for their families.</p>
  </div>

  <div class="feature abs" style="left:98px;top:3166px;width:490px">
    <h3>Where to start</h3>
    <p>We need to know what your issues are and how we can understand the personnal you require , over what time frame and the number of employees you need. Once this is estabilished we start sourcing workers in the Philippines that meet your criteria while starting the process in the UK to be able to have all the documents in place to deliver your company hard working skilled individuals.</p>
  </div>
  <div class="blob abs" style="left:650px;top:3060px;width:435px;height:340px;background:linear-gradient(135deg,#e7e4df,#9a9590 50%,#4a4744)" role="img" aria-label="Photo of a young man in a grey sweater with arms crossed"></div>
  <span class="cross abs" style="left:670px;top:3420px">×</span>

  <div class="blob abs" style="left:95px;top:3530px;width:435px;height:340px;background:linear-gradient(135deg,#4e5d74,#8b95a6 50%,#2a3345)" role="img" aria-label="Photo of a smiling man in a checked blazer looking at his phone"></div>
  <span class="ring abs" style="left:158px;top:3598px"></span>
  <div class="feature abs" style="left:613px;top:3625px;width:490px">
    <h3>Contact us today</h3>
    <p>Please contact us today with your requirements , this can be care workers ,chef, welders, pipe fitters, caravan cabinet makers, medical workers. The UK list of required skills is extensive and the Philippines offersenglish speaking highly qualified hard working employees. Contact us today and make that first step to a highly motivated , quality skilled workforce.</p>
  </div>
</section>

<section class="news abs">
  <div class="tag abs"><b>NEW</b>Cras efficitur tristique felis</div>
  <div class="news-photo abs" role="img" aria-label="Photo of businessmen talking together in a glass office"></div>
  <h2 class="abs">Vestibulum a<br>lectus ut rhoncus<br>augue velit</h2>
  <p class="lead abs">Please co today with your requirements this can be care woers ,chef, welders, pipe fitters, caravan cabinet madical</p>
  <span class="continue abs">CONTINUE READING <span class="arrow">→|</span></span>
  <div class="news-list abs">
    <div class="news-item"><div><small>Popular News</small><h4>Praesent imperdiet massa neque, id posuer</h4></div><span class="arrow">→|</span></div>
    <div class="news-item"><div><small>Popular News</small><h4>Praesent imperdiet massa neque, id posuer</h4></div><span class="arrow">→|</span></div>
    <div class="news-item"><div><small>Popular News</small><h4>Praesent imperdiet massa neque, id posuer</h4></div><span class="arrow">→|</span></div>
  </div>
</section>

<section class="contact">
  <div class="contact-head abs">
    <p class="eyebrow">Contact Us</p>
    <h2>Get In Touch</h2>
  </div>
  <div class="shy abs">
    <h3>Don’t be shy</h3>
    <p>Feel free to get in touch with us. Nam venenatis cursus libero ut congue. In sollicitudin ligula ipsum</p>
    <div class="reach">
      <svg width="24" height="18" viewBox="0 0 24 18"><rect x="1" y="1" width="22" height="16" rx="2" fill="#912f2c"/><path d="M2 2l10 8 10-8" stroke="#fff" stroke-width="2" fill="none"/></svg>
      <span>Mail us</span><span>info@brindlecrewstaffing.example.com</span>
    </div>
    <div class="reach">
      <svg width="22" height="22" viewBox="0 0 24 24"><path d="M6.6 10.8a15.1 15.1 0 006.6 6.6l2.2-2.2a1 1 0 011-.25 11.4 11.4 0 003.6.57 1 1 0 011 1V20a1 1 0 01-1 1A17 17 0 013 4a1 1 0 011-1h3.5a1 1 0 011 1c0 1.25.2 2.45.57 3.6a1 1 0 01-.25 1z" fill="#912f2c"/></svg>
      <span>Call us</span><span>1800 555 019</span>
    </div>
  </div>
  <div class="field f1 abs">First name</div>
  <div class="field f2 abs">Last name</div>
  <div class="field f3 abs">Email address</div>
  <div class="field f4 abs">Phone</div>
  <div class="field f5 abs">Youre message</div>
  <a class="btn btn-red submit abs" href="#">Submit <span class="arrow">→|</span></a>
</section>

<footer class="footer abs">
  <div class="logo abs"><span class="mark"></span>Brindle Crew Staffing</div>
  <span class="back-top abs">Back to Top ↑</span>
  <div class="footer-rule abs"></div>
  <div class="fcol col1 abs"><h4>Quick Links</h4><ul><li>Home</li><li>About</li><li>Services</li><li>Articles</li><li>Training</li><li>Contact us</li></ul></div>
  <div class="fcol col2 abs"><h4>Services</h4><ul><li>Civil engineer (professional)</li><li>Highways engineer</li><li>Petroleum engineer</li><li>Public health engineer</li><li>Site engineer</li></ul></div>
  <div class="fcol col3 abs">
    <h4>Subscribe to our<br>newsletter</h4>
    <div class="subscribe"><span>Email address</span><i>→</i></div>
    <div class="socials"><span></span><span></span><span></span></div>
  </div>
  <p class="copyright abs">© 2023 <b>Brindle Crew Staffing</b>. All right reserved</p>
  <p class="stamp abs">March 28,2023, Layout_4</p>
</footer>

</body>
</html>
```